Website for AV installation with booking system and e-commerce

Company: Corvexa
Tag Line: Audio Visual and Security System Installations
We need a website for an AV company based in Sydney Australia. We specialise in Audio Visual, CCTV (security cameras), and Data Cabling.
The purpose of the website is that customers book their installation online with a live booking system.
We are looking for the following:
- Creative and modern design
- easy to use - keep in mind that the user who will book will have little knowledge in technology.
- clean and organised
- colours to work in well with our logo we also like royal to navy blue, but we are open to other suggested what works well with our logo.
We want customers to be able to add products needed for their installation ie when booking to wall mount their TV they can choose to add a TV bracket and cables to the cart and vise-versa buy a bracket or cables and add to cart the installation.
Tabs to be included:
About us
Gallery
Contact Us
Home
Services (there are three services that we offer - Residential, Corporate and Retail)
Products
Book Online/Cart (checkout)
Temporary website checkout: www.corvexa.com.au, please note this is very basic and we do not want a copy of this. This is purely to give you an idea of our company.
Good Luck!
Target Market(s)
home owners/renters, business owners, archiects/designers, builders
Industry/Entity Type
E-Commerce
Look and feel

```html
<!DOCTYPE html>
<html lang="en">
<head>
<meta charset="utf-8">
<title>Corvexa – Audio Visual and Security System Installations</title>
<link href="https://fonts.googleapis.com/css2?family=Arimo:wght@400;700&family=Jura:wght@300;400;600&display=swap" rel="stylesheet">
<style>
:root{
  --red:#d4141c;
  --red-dark:#b80f16;
  --red-bright:#e81c24;
  --charcoal:#373c3d;
  --charcoal-2:#2f3435;
  --ink:#333;
  --muted:#555;
  --light:#efefef;
  --panel:#f6f6f6;
  --line:#c8c8c8;
  --white:#fff;
}
*{box-sizing:border-box;margin:0;padding:0}
html,body{width:680px;height:1200px;overflow:hidden}
body{position:relative;background:var(--white);font-family:"Arimo",Arial,sans-serif;color:var(--ink)}
.abs{position:absolute}
.display{font-family:"Jura","Arimo",sans-serif}

/* header */
.header{left:0;top:0;width:680px;height:65px;background:linear-gradient(#fff,#ececec);border-top:4px solid var(--red)}
.brand{left:55px;top:14px;font-size:30px;font-weight:700;color:var(--red);letter-spacing:-0.5px}
.cart-tab{left:518px;top:0;width:107px;height:18px;background:var(--red);border-radius:0 0 6px 6px;color:#fff;font-size:9px;display:flex;align-items:center;justify-content:center;gap:5px}
.social{top:34px;width:18px;height:18px;border-radius:2px}
.social.a{left:542px;background:#3b5a9a}
.social.b{left:564px;background:#2fa6dd}
.social.c{left:586px;background:#c8261d}

/* nav */
.nav{left:0;top:65px;width:680px;height:24px;background:linear-gradient(#454b4c,var(--charcoal-2))}
.nav a{position:absolute;top:0;height:24px;line-height:24px;color:#fff;font-size:10px;text-decoration:none}
.nav .home{left:55px;width:59px;text-align:center;background:var(--red)}
.phone{left:492px;top:68px;display:flex;align-items:center;gap:4px;color:#fff;font-size:16px;font-weight:700}

/* hero */
.hero{left:0;top:89px;width:680px;height:221px;background:linear-gradient(90deg,#f3f4f6,#e8eaee)}
.hero-photo{left:50px;top:30px;width:320px;height:150px;background:radial-gradient(ellipse at 30% 50%,#f0f0f0,#cfd1d4 60%,#e6e7ea)}
.hero-title{left:388px;top:55px;font-size:35px;font-weight:300;color:var(--red);letter-spacing:0.5px}
.hero-sub{left:388px;top:92px;font-size:15px;color:#555}
.hero-small{left:388px;top:110px;font-size:10.5px;color:#666}
.btn{background:linear-gradient(#e4262d,var(--red-dark));color:#fff;border-radius:3px;font-weight:700;display:flex;align-items:center;justify-content:center}
.learn{left:392px;top:132px;width:74px;height:22px;font-size:10px}
.arrow{width:20px;height:30px}

/* red band */
.band{left:0;top:310px;width:680px;height:190px;background:var(--red);overflow:hidden}
.band-photo{left:420px;top:0;width:260px;height:190px;background:linear-gradient(120deg,var(--red) 0%,#c01017 40%,#e8555a 100%)}
.band-title{left:55px;top:26px;font-size:32px;font-weight:300;color:#fff;letter-spacing:0.3px}
.band-sub{left:55px;top:60px;font-size:19px;font-weight:300;color:#fff}
.band-text{left:55px;top:90px;width:365px;font-size:8.4px;line-height:13px;color:#fff}

/* products */
.products{left:0;top:500px;width:680px;height:220px;background:var(--charcoal)}
.card{top:22px;width:112px;height:176px;background:var(--red-bright);border:1px solid #f34a50}
.card h3{position:absolute;top:7px;width:100%;text-align:center;font-family:"Jura",sans-serif;font-weight:400;font-size:14px;color:#fff}
.card .thumb{position:absolute;left:5px;top:29px;width:101px;height:77px}
.card .desc{position:absolute;top:113px;width:100%;text-align:center;color:#fff;font-size:6.8px;font-weight:700;line-height:9px}
.card .price{position:absolute;top:135px;width:100%;text-align:center;color:#fff;font-family:"Jura",sans-serif;font-size:10px}
.card .add{position:absolute;left:26px;top:150px;width:59px;height:16px;background:linear-gradient(#fff,#ddd);border-radius:2px;font-size:6.5px;color:#333;display:flex;align-items:center;justify-content:center;gap:3px}

/* features */
.features{left:0;top:720px;width:680px;height:198px;background:var(--light)}
.features h2{position:absolute;left:61px;top:22px;font-family:"Jura",sans-serif;font-weight:600;font-size:17px;color:#333}
.feat{width:255px}
.feat .num{position:absolute;left:0;top:0;width:12px;height:12px;background:var(--red-dark);color:#fff;font-size:8px;text-align:center;line-height:12px}
.feat h4{position:absolute;left:21px;top:0;font-size:9.5px;font-weight:400;color:var(--red);white-space:nowrap}
.feat p{position:absolute;left:21px;top:15px;width:240px;font-size:7.3px;line-height:10px;color:var(--muted)}
.divider{top:830px;height:1px;background:#d6d6d6}

/* booking */
.booking{left:0;top:918px;width:680px;height:197px;background:#e6e6e6}
.booking h2{position:absolute;left:70px;top:9px;font-family:"Jura",sans-serif;font-weight:400;font-size:18px;color:#444}
.booking h2 em{font-style:normal;font-weight:600;color:var(--red)}
.panel{left:55px;top:959px;width:570px;height:156px;background:var(--panel);box-shadow:0 0 4px rgba(0,0,0,.12)}
.lbl{font-size:7px;color:#333;white-space:nowrap}
.req{color:var(--red)}
.field{background:#e9e9e9;border:1px solid #c2c2c2}
.select{background:#e6e6e6;border:1px solid #b6b6b6;font-size:6.5px;color:#666;padding-left:3px;line-height:11px}
.select span{position:absolute;right:1px;top:1px;width:9px;height:9px;border:1px solid #888;background:#fff}
.chk{width:7px;height:7px;border:1px solid #999;background:#fff}
.captcha{left:446px;top:1038px;width:74px;height:15px;background:#e3e3e3;border:1px solid #bbb;font-size:10px;letter-spacing:4px;text-align:center;line-height:13px;color:#333}
.send{left:531px;top:1075px;width:41px;height:17px;font-size:10px}

/* footer */
.foot-note{left:0;top:1115px;width:680px;height:43px;background:#dcdcdc;text-align:center;font-size:7.2px;line-height:9.5px;color:#444;padding-top:7px}
.footer{left:0;top:1158px;width:680px;height:42px;background:var(--charcoal)}
.footer .links{position:absolute;left:56px;top:10px;font-size:7px;color:#ccc}
.footer .copy{position:absolute;left:56px;top:24px;font-size:6px;color:#bbb}
.footer .brand-foot{position:absolute;left:512px;top:7px;font-size:24px;font-weight:700;color:var(--red)}
</style>
</head>
<body>

<header class="abs header"></header>
<div class="abs brand">Corvexa</div>
<div class="abs cart-tab">
  <svg width="10" height="9" viewBox="0 0 10 9"><path d="M0 1h2l1.5 5h5L10 2.5H3" fill="none" stroke="#fff" stroke-width="1"/><circle cx="4" cy="7.8" r=".9" fill="#fff"/><circle cx="8" cy="7.8" r=".9" fill="#fff"/></svg>
  0 Items on cart
</div>
<div class="abs social a" role="img" aria-label="Social link"></div>
<div class="abs social b" role="img" aria-label="Social link"></div>
<div class="abs social c" role="img" aria-label="Social link"></div>

<nav class="abs nav">
  <a class="home" href="#">Home</a>
  <a href="#" style="left:125px">About Us</a>
  <a href="#" style="left:191px">Gallery</a>
  <a href="#" style="left:249px">Services</a>
  <a href="#" style="left:312px">Products</a>
  <a href="#" style="left:377px">Contact Us</a>
</nav>
<div class="abs phone">
  <svg width="11" height="14" viewBox="0 0 11 14"><rect x="0.5" y="0.5" width="10" height="13" rx="1.5" fill="var(--red)"/><rect x="2" y="2" width="7" height="4" fill="#fff"/><g fill="#fff"><rect x="2" y="7.5" width="1.6" height="1.4"/><rect x="4.7" y="7.5" width="1.6" height="1.4"/><rect x="7.4" y="7.5" width="1.6" height="1.4"/><rect x="2" y="10" width="1.6" height="1.4"/><rect x="4.7" y="10" width="1.6" height="1.4"/><rect x="7.4" y="10" width="1.6" height="1.4"/></g></svg>
  0-000-000-0000
</div>

<section class="abs hero">
  <div class="abs hero-photo" role="img" aria-label="Two dome security cameras, white and dark grey"></div>
  <div class="abs display hero-title">LOREM IPSUM</div>
  <div class="abs display hero-sub">consectetur adipiscing elit. Nulla</div>
  <div class="abs display hero-small">lobortis consequat mauris, eget eleifend nunc</div>
  <div class="abs btn learn">Learn More</div>
  <svg class="abs arrow" style="left:14px;top:95px" viewBox="0 0 20 30"><path d="M16 2L4 15l12 13" fill="none" stroke="var(--red)" stroke-width="4"/></svg>
  <svg class="abs arrow" style="left:646px;top:95px" viewBox="0 0 20 30"><path d="M4 2l12 13L4 28" fill="none" stroke="var(--red)" stroke-width="4"/></svg>
</section>

<section class="abs band">
  <div class="abs band-photo" role="img" aria-label="Red network data cables with plugs"></div>
  <div class="abs display band-title">DONEC A LECTUS NON PURUS</div>
  <div class="abs display band-sub">eleifend. Duis nec augue eget lorem vestibulum</div>
  <p class="abs band-text">suscipit. Integer eget ligula lectus, eget pulvinar diam. Donec porttitor viverra nibh ac pulvinar. Pellentesque habitant morbi tristique senectus et netus et malesuada fames ac turpis egestas. Phasellus mollis pharetra dignissim. Ut pretium blandit lectus congue fringilla. Aliquam imper-diet ante quis odio congue ultrices. Donec at nisl augue, sit amet ultricies leo. Cras viverra lacinia magna, auctor convallis sapien interdum at</p>
</section>

<section class="abs products">
  <svg class="abs arrow" style="left:24px;top:105px" viewBox="0 0 20 30"><path d="M16 2L4 15l12 13" fill="none" stroke="var(--red)" stroke-width="4"/></svg>
  <svg class="abs arrow" style="left:636px;top:105px" viewBox="0 0 20 30"><path d="M4 2l12 13L4 28" fill="none" stroke="var(--red)" stroke-width="4"/></svg>

  <article class="abs card" style="left:56px">
    <h3>Nulla lobortis</h3>
    <div class="thumb" role="img" aria-label="TV on a wooden media cabinet" style="background:linear-gradient(#f2f2f2 20%,#9a6a3c 20%,#7c5229)"></div>
    <div class="desc">Donec a lectus non<br>purus ultricies eleifend. Duis</div>
    <div class="price">Price: $000.00</div>
    <div class="add"><svg width="8" height="7" viewBox="0 0 10 9"><path d="M0 1h2l1.5 5h5L10 2.5H3" fill="none" stroke="#333"/></svg>Add to Cart</div>
  </article>
  <article class="abs card" style="left:170.5px">
    <h3>Nulla lobortis</h3>
    <div class="thumb" role="img" aria-label="Living room with wall mounted TV" style="background:linear-gradient(#9a9a9a,#cfcfcf 60%,#a88e70)"></div>
    <div class="desc">Donec a lectus non<br>purus ultricies eleifend. Duis</div>
    <div class="price">Price: $000.00</div>
    <div class="add"><svg width="8" height="7" viewBox="0 0 10 9"><path d="M0 1h2l1.5 5h5L10 2.5H3" fill="none" stroke="#333"/></svg>Add to Cart</div>
  </article>
  <article class="abs card" style="left:285px">
    <h3>Nulla lobortis</h3>
    <div class="thumb" role="img" aria-label="Home theatre with speakers and screen" style="background:linear-gradient(#f4f4f4,#d8d8d8 70%,#555)"></div>
    <div class="desc">Donec a lectus non<br>purus ultricies eleifend. Duis</div>
    <div class="price">Price: $000.00</div>
    <div class="add"><svg width="8" height="7" viewBox="0 0 10 9"><path d="M0 1h2l1.5 5h5L10 2.5H3" fill="none" stroke="#333"/></svg>Add to Cart</div>
  </article>
  <article class="abs card" style="left:399.5px">
    <h3>Nulla lobortis</h3>
    <div class="thumb" role="img" aria-label="Boardroom with projection screen" style="background:linear-gradient(#fafafa,#e2e2e2 60%,#9c9c9c)"></div>
    <div class="desc">Donec a lectus non<br>purus ultricies eleifend. Duis</div>
    <div class="price">Price: $000.00</div>
    <div class="add"><svg width="8" height="7" viewBox="0 0 10 9"><path d="M0 1h2l1.5 5h5L10 2.5H3" fill="none" stroke="#333"/></svg>Add to Cart</div>
  </article>
  <article class="abs card" style="left:514px">
    <h3>Nulla lobortis</h3>
    <div class="thumb" role="img" aria-label="Wall mounted security camera" style="background:radial-gradient(circle at 45% 45%,#fff,#d0d0d0 70%)"></div>
    <div class="desc">Donec a lectus non<br>purus ultricies eleifend. Duis</div>
    <div class="price">Price: $000.00</div>
    <div class="add"><svg width="8" height="7" viewBox="0 0 10 9"><path d="M0 1h2l1.5 5h5L10 2.5H3" fill="none" stroke="#333"/></svg>Add to Cart</div>
  </article>
</section>

<section class="abs features">
  <h2>Integer eget ligula lectus</h2>
</section>
<div class="abs feat" style="left:63px;top:779px">
  <span class="num">1</span><h4>Lorem ipsum dolor sit amet, consectetur adipiscing</h4>
  <p>Nulla lobortis consequat mauris, eget eleifend nunc viverra viverra. Ut ac risus odio. Aliquam pretium purus sed nulla feugiat blandit.</p>
</div>
<div class="abs feat" style="left:363px;top:779px">
  <span class="num">2</span><h4>Ipsum dolor sit amet, consectetur adipiscing</h4>
  <p>Lobortis consequat mauris, eget eleifend nunc viverra viverra. Ut ac risus odio. Aliquam pretium purus sed nulla feugiat blandit.</p>
</div>
<div class="abs divider" style="left:58px;width:272px"></div>
<div class="abs divider" style="left:358px;width:270px"></div>
<div class="abs feat" style="left:63px;top:846px">
  <span class="num">3</span><h4>Lorem ipsum dolor sit amet, consectetur</h4>
  <p>Consequat mauris, eget eleifend nunc viverra viverra. Ut ac risus odio. Aliquam pretium purus sed nulla feugiat blandit.</p>
</div>
<div class="abs feat" style="left:363px;top:846px">
  <span class="num">4</span><h4>Lorem ipsum dolor sit amet, consectetur adipiscing</h4>
  <p>Nulla lobortis consequat mauris, eget eleifend nunc viverra viverra. Ut ac risus odio. Aliquam pretium purus sed nulla feugiat blandit.</p>
</div>

<section class="abs booking">
  <h2>Book your <em>installation</em> online</h2>
</section>
<form class="abs panel"></form>

<span class="abs lbl" style="left:73px;top:979px">First Name: <span class="req">*</span></span>
<span class="abs lbl" style="left:73px;top:996px">Last Name: <span class="req">*</span></span>
<span class="abs lbl" style="left:73px;top:1013px">Company:</span>
<span class="abs lbl" style="left:73px;top:1031px">eMail: <span class="req">*</span></span>
<span class="abs lbl" style="left:73px;top:1048px">Phone: <span class="req">*</span></span>
<div class="abs field" style="left:117px;top:977px;width:93px;height:12px"></div>
<div class="abs field" style="left:117px;top:995px;width:93px;height:12px"></div>
<div class="abs field" style="left:117px;top:1012px;width:93px;height:12px"></div>
<div class="abs field" style="left:117px;top:1029px;width:93px;height:12px"></div>
<div class="abs field" style="left:117px;top:1047px;width:93px;height:12px"></div>

<span class="abs lbl" style="left:248px;top:979px">Time to Call: <span class="req">*</span></span>
<div class="abs select" style="left:316px;top:977px;width:92px;height:12px">Morning<span></span></div>
<span class="abs lbl" style="left:248px;top:995px">Address:</span>
<div class="abs field" style="left:316px;top:994px;width:92px;height:27px"></div>
<span class="abs lbl" style="left:248px;top:1030px">Nature Of Business:</span>
<div class="abs field" style="left:316px;top:1028px;width:92px;height:27px"></div>

<span class="abs lbl" style="left:446px;top:980px">Number Of Employees :</span>
<div class="abs select" style="left:537px;top:978px;width:40px;height:12px">1-10<span></span></div>
<span class="abs lbl" style="left:446px;top:1004px">What Options Interest You :</span>
<div class="abs chk" style="left:537px;top:1005px"></div><span class="abs lbl" style="left:549px;top:1004px">IT Services</span>
<div class="abs chk" style="left:537px;top:1015px"></div><span class="abs lbl" style="left:549px;top:1014px">Hardware Purchase</span>
<div class="abs chk" style="left:537px;top:1025px"></div><span class="abs lbl" style="left:549px;top:1024px">IT Security</span>
<div class="abs chk" style="left:537px;top:1036px"></div><span class="abs lbl" style="left:549px;top:1035px">Network Review</span>
<div class="abs chk" style="left:537px;top:1046px"></div><span class="abs lbl" style="left:549px;top:1045px">Computer Repair</span>
<span class="abs lbl" style="left:446px;top:1027px"><span class="req">*</span> Modify Field</span>
<div class="abs captcha">5623</div>
<span class="abs lbl" style="left:446px;top:1065px">Please enter the code</span>
<div class="abs field" style="left:446px;top:1075px;width:74px;height:14px"></div>
<div class="abs btn send">Send</div>

<div class="abs foot-note">Consequat mauris, eget eleifend nunc viverra viverra.<br>Ut ac risus odio. Aliquam pretium purus<br>sed nulla feugiat blandit.</div>

<footer class="abs footer">
  <div class="links">About Us &nbsp;|&nbsp; Privacy Policy &nbsp;|&nbsp; Terms Of Use</div>
  <div class="copy">Copyright Information 2013</div>
  <div class="brand-foot">Corvexa</div>
</footer>

</body>
</html>
```